Small company security and risk consulting startup needs an explosive message via marketing colla...

Need a two page (front/back) flyer that calls out our three primary service areas incorporating brandmill developed logo and website visuals. Something that grabs attention at first glance to entice the viewer to read and connect for a services consultation. I will need the ability to make minor adjustments and add language.

```html
<!DOCTYPE html>
<html lang="en">
<head>
<meta charset="utf-8">
<title>Keystone Shield – Security Consulting Flyer</title>
<link rel="stylesheet" href="https://fonts.googleapis.com/css2?family=Lato:ital,wght@0,300;0,400;0,700;0,900;1,300;1,400&family=Montserrat:wght@800;900&display=swap">
<style>
:root{
  --red:#e3222a;
  --red-deep:#9e1317;
  --navy:#0b1a33;
  --ink:#2b2b2b;
  --grey-text:#6d6d78;
  --panel:#ededee;
  --white:#ffffff;
  --stage:#5b628f;
  --blue-badge:#2a4aa0;
}
*{margin:0;padding:0;box-sizing:border-box}
html,body{width:1200px;height:842px;overflow:hidden}
body{background:var(--stage);font-family:"Lato",sans-serif;color:var(--ink);position:relative}
.page{position:absolute;top:107px;width:443px;height:620px;background:var(--white);overflow:hidden;box-shadow:0 6px 18px rgba(0,0,0,.25)}
.page--front{left:130px}
.page--back{left:627px}
.abs{position:absolute}
svg.shape{position:absolute;left:0;top:0}

/* brand lockup */
.brand{position:absolute;text-align:center}
.brand__mark{display:inline-block;width:9px;height:9px;background:var(--red);vertical-align:middle;margin-right:4px}
.brand__name{font-weight:900;font-size:14px;color:var(--red);vertical-align:middle}
.brand__tag{display:block;font-weight:700;font-size:4.6px;letter-spacing:2.2px;color:var(--ink);margin-top:2px}
.badge{position:absolute;border-radius:50%;background:var(--white);border:3px solid var(--blue-badge)}

/* front header */
.contact-phone{right:62px;top:18px;font-weight:900;font-size:24px;color:var(--red);letter-spacing:-.3px}
.contact-web{right:62px;top:47px;font-size:10.5px;color:var(--ink)}
.photo{position:absolute}
.headline{left:44px;top:116px}
.headline span{display:inline-block;background:var(--red);color:var(--white);font-weight:700;font-size:21.5px;line-height:25px;padding:1px 5px;margin-bottom:2px}
.subline{left:51px;top:177px;font-style:italic;font-weight:300;font-size:8.6px;line-height:11px;color:var(--white)}

.section-title{font-weight:700;font-size:11.5px;color:var(--white)}
.rule{display:block;width:35px;height:1.5px;background:var(--white);margin-top:4px}
.body-sm{font-size:5.6px;line-height:10px}
.services-intro{left:37px;top:365px;width:152px;color:var(--white)}
.service{position:absolute;left:37px;width:160px}
.service__icon{position:absolute;left:0;top:2px;width:26px;height:26px;border-radius:4px;background:var(--white)}
.service__title{margin-left:35px;font-weight:700;font-size:8.6px;line-height:9px;color:var(--white)}
.service__text{margin-left:35px;color:var(--white);margin-top:2px}

.about{left:252px;top:393px;width:155px;color:var(--grey-text)}
.about h2{font-weight:900;font-size:14px;color:var(--red);letter-spacing:.5px;margin-bottom:3px}
.about .rule{background:var(--red);width:14px;margin:0 0 12px}
.about ul{list-style:none;margin-top:8px}
.about li{position:relative;padding-left:14px;margin-bottom:10px}
.about li::before{content:"»";position:absolute;left:0;top:0;color:#6ab04c;font-size:6px}

/* back page */
.title-big{left:24px;top:170px;font-family:"Montserrat",sans-serif;font-weight:900;font-size:26px;line-height:25px;color:var(--white);letter-spacing:.3px}
.title-big .rule{width:80px;height:1.6px;margin-top:6px}
.title-sub{left:23px;top:238px;font-style:italic;font-weight:300;font-size:8.2px;line-height:12px;color:var(--white)}
.who{left:35px;top:342px;width:150px;color:var(--ink)}
.who h3,.review h3,.consult h3{font-weight:900;font-size:11px;color:var(--ink)}
.who .rule,.review .rule,.consult .rule{background:var(--red);width:22px;margin:3px 0 12px}
.who p{margin-bottom:10px}
.review{left:258px;top:258px;width:160px}
.review h3{font-size:11px;line-height:14px}
.consult{left:258px;top:377px;width:165px}
.consult h3{font-size:8.2px}
.consult .rule{margin:1px 0 9px}
.review p,.consult p{color:#444}
.foot-pin{position:absolute;width:22px;height:22px;background:var(--red);border-radius:50%}
.foot-text{font-size:9.5px;line-height:11px;color:var(--ink)}
.foot-web{font-size:7.4px}
</style>
</head>
<body>

<!-- FRONT -->
<section class="page page--front">
  <div class="brand" style="left:14px;top:50px">
    <span class="brand__mark"></span><span class="brand__name">Keystone Shield</span>
    <span class="brand__tag">CONSULTING SERVICES</span>
  </div>
  <div class="abs contact-phone">+1 555 014 2290</div>
  <div class="abs contact-web">www.keystoneshield.com</div>
  <div class="badge" style="left:389px;top:17px;width:44px;height:44px"></div>

  <svg class="shape" width="443" height="84" viewBox="0 0 443 84">
    <polygon points="150,84 162,72 443,72 443,84" fill="var(--red)"/>
  </svg>

  <div class="photo" role="img" aria-label="Smiling woman holding a payment tablet in a server room" style="left:0;top:84px;width:443px;height:295px;background:linear-gradient(100deg,#0d2a55 0%,#1c4f8a 35%,#5c5f6a 62%,#2a3550 100%)"></div>

  <svg class="shape" width="443" height="620" viewBox="0 0 443 620">
    <defs>
      <linearGradient id="frontRed" x1="0" y1="0" x2="1" y2="1">
        <stop offset="0" stop-color="var(--red-deep)"/>
        <stop offset="1" stop-color="var(--red)"/>
      </linearGradient>
    </defs>
    <polygon points="0,200 221,378 221,620 0,620" fill="url(#frontRed)"/>
    <polygon points="221,378 443,378 443,620 221,620" fill="var(--white)"/>
    <polygon points="405,610 443,610 443,620 415,620" fill="var(--red)"/>
    <polygon points="221,610 405,610 415,620 221,620" fill="var(--red-deep)"/>
  </svg>

  <div class="abs headline"><span>The Global Managed</span><br><span>Security Experts</span></div>
  <div class="abs subline">Extend Your Security Team with Our miss and have the<br>Best Security Specialists Working For You</div>

  <div class="abs" style="left:37px;top:340px">
    <div class="section-title">OUR SERVICES</div><span class="rule"></span>
  </div>
  <p class="abs body-sm services-intro">Curabitur vehicula tellus ut leo vulputate placerat. Morbi ullamcorper est ultricies justo vulputate congue. Mauris sed libero nulla. Ut vulputate lacus nec mi fermentum, ut accumsan ex mattis.</p>

  <div class="service" style="top:426px">
    <svg class="service__icon" viewBox="0 0 26 26"><rect x="6" y="7" width="14" height="9" fill="none" stroke="#222" stroke-width="1"/><line x1="10" y1="19" x2="16" y2="19" stroke="#222"/></svg>
    <div class="service__title">NATIONAL SECURITY</div>
    <p class="body-sm service__text">Curabitur vehicula tellus ut leo vulputate placerat. Morbi ullamcorper est ultricies justo vulputate congue. Mauris sed libero nulla.</p>
  </div>
  <div class="service" style="top:480px">
    <svg class="service__icon" viewBox="0 0 26 26"><polygon points="7,18 12,8 17,18" fill="none" stroke="#222"/><circle cx="18" cy="9" r="3" fill="none" stroke="#222"/></svg>
    <div class="service__title">RISK MANAGEMENT<br>SERVICE</div>
    <p class="body-sm service__text">Curabitur vehicula tellus ut leo vulputate placerat. Morbi ullamcorper est ultricies justo</p>
  </div>
  <div class="service" style="top:534px">
    <svg class="service__icon" viewBox="0 0 26 26"><rect x="6" y="6" width="9" height="7" fill="none" stroke="#222"/><rect x="11" y="12" width="9" height="7" fill="none" stroke="#222"/></svg>
    <div class="service__title">CONSULTING SERVICE</div>
    <p class="body-sm service__text">Curabitur vehicula tellus ut leo vulputate placerat. Morbi ullamcorper est ultricies justo vulputate congue. Mauris sed libero nulla.</p>
  </div>

  <div class="abs about body-sm">
    <h2>ABOUT US</h2><span class="rule"></span>
    <p>Nulla quam nibh, lobortis ac dapibus ut, feugiat at nisi. Sed et sem vel nisi tempus tempus id eget ex. Fusce et felis feugiat, volutpat dolor vitae, maximus erat.</p>
    <ul>
      <li>Pellentesque nec erat porttitor, auctor dolor a, dictum urna. Etiam ut sapien venenatis, facilisis odio et.</li>
      <li>Integer dui eros, consectetur non posuere non, sollicitudin ac ligula.</li>
      <li>Donec bibendum feugiat augue, ut semper urna blandit aliquet. Cras nunc justo, laoreet sed posuere. Quisque sollicitudin tortor vel massa feugiat.</li>
    </ul>
  </div>
</section>

<!-- BACK -->
<section class="page page--back">
  <div class="photo" role="img" aria-label="Digital network globe with data dashboards" style="left:0;top:0;width:443px;height:230px;background:radial-gradient(ellipse at 60% 45%,#3f7fb8 0%,#163a66 40%,#071428 100%)"></div>

  <svg class="shape" width="443" height="620" viewBox="0 0 443 620">
    <defs>
      <linearGradient id="backRed" x1="0" y1="0" x2="1" y2="1">
        <stop offset="0" stop-color="var(--red-deep)"/>
        <stop offset="1" stop-color="var(--red)"/>
      </linearGradient>
    </defs>
    <polygon points="0,230 443,230 443,620 0,620" fill="var(--white)"/>
    <polygon points="312,214 443,198 443,537 215,537 215,255" fill="var(--panel)"/>
    <polygon points="0,105 312,214 0,343" fill="url(#backRed)"/>
    <polygon points="155,620 170,606 443,606 443,620" fill="var(--red)"/>
  </svg>

  <div class="abs title-big">SECURITY<br>CONSULTING<span class="rule"></span></div>
  <p class="abs title-sub">Our consultants and cybersecurity experts help your organization<br>adapt, mitigate risk and thrive in the evolving threat<br>and regulatory compliance landscape</p>

  <div class="abs who body-sm">
    <h3>WHE WE ARE</h3><span class="rule"></span>
    <p>Maecenas congue ex tellus, id blandit ligula sodales eget. Fusce vel justo nisi. Etiam tincidunt nibh vel sem tempor, vel facilisis metus sodales. Suspendisse potenti.</p>
    <p>Curabitur vehicula tellus ut leo vulputate placerat. Morbi ullamcorper est ultricies justo vulputate congue. Mauris sed libero nulla. Ut vulputate lacus nec mi fermentum, ut accumsan ex mattis. Morbi dignissim sem ac cursus sodales. Donec ornare turpis congue semper tempus.</p>
    <p>Mauris nisl elit, consectetur at facilisis ut, posuere in orci. Nam congue tristique ipsum eget finibus. Sed dapibus rutrum erat eu viverra. In consectetur euismod odio sit amet iaculis. Proin ut lacinia libero. Aenean nec sapien nulla acerat dictum eu id justo.</p>
  </div>

  <div class="abs review body-sm">
    <h3>THE DECISION-MAKING PROCESS OFF STRATEGIC DEFENCE AND SECURTY REVIEW</h3><span class="rule"></span>
    <p>Curabitur vehicula tellus ut leo vulputate placerat. Morbi ullamcorper est ultricies justo vulputate congue. Mauris sed libero nulla. Ut vulputate lacus nec mi fermentum, ut accumsan ex mattis.</p>
  </div>
  <div class="abs consult body-sm">
    <h3>SECURITY CONSULTING SERVICES</h3><span class="rule"></span>
    <p>Professional security consultants can be the solution to the dilemma of not having enough knowledge and expertise to handle the latest cyber attacks, threats, and vulnerabilities. Whether it is gaining a clear understanding of your organization's security posture or the latest regulation to comply with, CISOs and other IT executives alike are challenged to stay above the fray and balance compliance needs and security costs. Our Security Consulting Services offers the expertise and proven recommendations to help you enhance your IT security posture, reduce your information security risk, facilitate compliance and improve your</p>
  </div>

  <div class="brand" style="left:20px;top:578px">
    <span class="brand__mark"></span><span class="brand__name">Keystone Shield</span>
    <span class="brand__tag">CONSULTING SERVICES</span>
  </div>

  <svg class="foot-pin" style="left:203px;top:552px" viewBox="0 0 22 22"><circle cx="11" cy="11" r="11" fill="var(--red)"/><path d="M11 5a4 4 0 0 1 4 4c0 3-4 8-4 8s-4-5-4-8a4 4 0 0 1 4-4z" fill="#fff"/><circle cx="11" cy="9" r="1.5" fill="var(--red)"/></svg>
  <div class="abs foot-text" style="left:232px;top:553px">48 Harbor Lane, Suite 7<br>Austin 73301 TX</div>
  <svg class="foot-pin" style="left:203px;top:578px" viewBox="0 0 22 22"><circle cx="11" cy="11" r="11" fill="var(--red)"/><path d="M8 6l2 3-1.5 1.5a7 7 0 0 0 3 3L13 12l3 2-1 2c-4 0-8-4-8-8z" fill="#fff"/></svg>
  <div class="abs foot-text" style="left:232px;top:580px;font-size:11.5px;font-weight:700">+1 555 014 2290<br><span class="foot-web" style="font-weight:400">www.keystoneshield.com</span></div>

  <div class="badge" style="left:360px;top:548px;width:58px;height:58px"></div>
</section>

</body>
</html>
```